Brightpath EAP 2 x Flyer with Poster

Brightpath is an award-winning organisation providing dynamic and creative ways for children, young people, adults and families to make positive change and achieve fulfilling lives.
We are launching into a new area of business and starting to offer organisations Employee Assistance Program (EAP). To launch this service we need 2 flyers and a poster:
- 1 x flyer for employers
- 1 x flyer for employees
- 1 x poster (A3) for employees to be displayed around the office.
For the flyers we are after an a4 colour double sided flyer in either a A4 tri-fold to DL format or A4 bi-fold to A5 format. We are looking for a design that is simple and dynamic whilst keeping in line with our branding.
The winning designs will need to be hi-res and ready for print and also a lower res version suitable to email.
I have attached a number of files to provide further background, including:
• I have attached 3 x word doc of copy for each (2 x flyer / 1 x poster)
• Brand Guidelines
• Logo
• Our clinic flyer recently produced by a ArtHive designer for our clinic area of the business. These flyers do not have to be exactly the same as this one but should appear to be from the same organisation although a different service.
Generally we like our designs to be clear and simple.
Please don't hesitate to reach out with any Q's.

```html
<!DOCTYPE html>
<html lang="en">
<head>
<meta charset="utf-8">
<title>Brightpath EAP Flyer</title>
<link href="https://fonts.googleapis.com/css2?family=Lato:wght@300;400;700&display=swap" rel="stylesheet">
<style>
:root{
  --bg:#cfcfcf;
  --sage:#739d8f;
  --sage-dark:#648c86;
  --teal:#6b8f92;
  --salmon:#d3aa97;
  --salmon-soft:#ecd6cb;
  --ink:#3a3a3a;
  --body:#5b5b5b;
  --white:#ffffff;
}
*{margin:0;padding:0;box-sizing:border-box}
html,body{width:904px;height:1200px;overflow:hidden;background:var(--bg);font-family:'Lato',sans-serif;color:var(--body)}
.sheet{position:absolute;left:80px;width:744px;height:525px;overflow:hidden}
.outside{top:58px;background:var(--sage)}
.inside{top:615px;background:var(--white)}
.abs{position:absolute}

/* outside */
.about-title{left:23px;top:38px;color:var(--white);font-weight:700;font-size:15px;letter-spacing:.2px}
.about-copy{left:23px;top:79px;width:325px;color:#eef3f1;font-weight:300;font-size:9.4px;line-height:12.7px;text-align:justify}
.about-copy p{margin-bottom:12px}
.logo-band{left:0;top:322px;width:371px;height:60px;background:var(--white);display:flex;align-items:center;justify-content:center;gap:9px}
.brand-mark{width:24px;height:24px;background:var(--sage)}
.brand-mark.light{background:var(--white)}
.brand-name{font-weight:700;font-size:30px;line-height:32px;color:var(--ink)}
.brand-name.light{color:var(--white)}
.contact{left:0;width:371px;text-align:center;color:#eef3f1;font-weight:300;font-size:10px;line-height:13px}
.contact-phone{font-weight:400;font-size:10.5px}
.logo-right{left:406px;top:72px;display:flex;align-items:center;gap:8px}
.logo-right .brand-mark{width:22px;height:22px}
.logo-right .brand-name{font-size:27px;line-height:28px}
.web-band{left:371px;top:461px;width:373px;height:64px;background:var(--salmon);display:flex;align-items:center;justify-content:center;font-weight:700;font-size:11px;letter-spacing:2.2px;color:var(--ink)}
.photos{left:0;top:0}

/* inside */
.tab{height:26px;display:flex;align-items:center;padding-left:24px;color:var(--white);font-weight:400;font-size:10px;letter-spacing:.1px}
.tab-sage{background:var(--sage);clip-path:polygon(0 0,100% 0,90% 100%,0 100%)}
.tab-teal{background:var(--teal);clip-path:polygon(0 0,100% 0,92% 100%,0 100%)}
.tab-salmon{background:var(--salmon);color:var(--ink);clip-path:polygon(0 0,100% 0,92% 100%,0 100%)}
.copy{font-weight:300;font-size:7.6px;line-height:10.2px;color:var(--body)}
.copy p{margin-bottom:10px}
.lead{font-size:10px;line-height:13px;color:var(--ink);font-weight:400}
.issues{display:flex;gap:14px;font-size:7.8px;color:var(--ink)}
.issues ul{list-style:none}
.issues li{height:16px}
.issues li::before{content:"> "}
.confidential-block{left:371px;top:112px;width:373px;height:225px;background:linear-gradient(180deg,var(--salmon-soft) 0%,var(--salmon) 100%);border-bottom-right-radius:40px}
.conf-list{list-style:none}
.conf-list li{margin-bottom:8px}
.conf-list .sub{padding-left:32px}
.photo-fade{left:371px;top:330px;width:373px;height:195px;background:linear-gradient(180deg,#f2f2f2 0%,#e4e4e4 60%,#d9d9d9 100%)}
</style>
</head>
<body>

<section class="sheet outside">
  <h2 class="abs about-title">ABOUT BRIGHTPATH</h2>
  <div class="abs about-copy">
    <p>Brightpath provides dynamic and creative ways for children, young people, adults and families to make positive change and achieve fulfilling lives.</p>
    <p>Brightpath is a registered NDIS provider with significant experience working in the disability and mental health sectors. We provide Positive Behaviour Support, Specialist and Support Coordination Services and NDIS Therapy and work with participants that use behaviours of concern. Our collective experience includes working with people with intellectual disability, cognitive impairment, neurodiversity and dual disability across a range of settings including institutions, supported accommodation, day programs, employment services, schools, family homes and community locations. We work with a trauma-informed lens using a person-centred approach.</p>
    <p>We provide tailored training and e-learning to individuals, families and service providers within the health and community services sectors and operate a psychology clinic in Northvale, Melbourne.</p>
  </div>

  <div class="abs logo-band">
    <span class="brand-mark"></span>
    <span class="brand-name">Brightpath</span>
  </div>

  <svg class="abs" style="left:175px;top:405px" width="20" height="22" viewBox="0 0 20 22" aria-hidden="true">
    <path d="M10 1a6 6 0 0 0-6 6c0 4.5 6 10 6 10s6-5.5 6-10a6 6 0 0 0-6-6z" fill="none" stroke="#fff" stroke-width="1.4"/>
    <circle cx="10" cy="7" r="2" fill="#fff"/>
    <path d="M2 21l4-5h8l4 5z" fill="#fff" opacity=".85"/>
  </svg>
  <div class="abs contact" style="top:430px">Harbourview Building<br>42 Lantern Way, Northvale VIC 3999</div>
  <div class="abs contact contact-phone" style="top:469px">(03) 9000 1234</div>
  <div class="abs contact" style="top:495px">hello@brightpath.example | brightpath.example</div>

  <div class="abs logo-right">
    <span class="brand-mark light"></span>
    <span class="brand-name light">Brightpath</span>
  </div>

  <svg class="abs photos" width="744" height="525" viewBox="0 0 744 525">
    <defs>
      <linearGradient id="handsTone" x1="0" y1="0" x2="1" y2="1">
        <stop offset="0" stop-color="#b7c3cc"/>
        <stop offset=".5" stop-color="#e3c7b4"/>
        <stop offset="1" stop-color="#a9b4bf"/>
      </linearGradient>
      <linearGradient id="sleeveTone" x1="0" y1="0" x2="1" y2="1">
        <stop offset="0" stop-color="#c7ced6"/>
        <stop offset="1" stop-color="#2c3344"/>
      </linearGradient>
    </defs>
    <polygon role="img" aria-label="Photo of stacked hands joined together in teamwork" points="404,158 583,158 639,304 578,459 409,459 484,308" fill="url(#handsTone)" stroke="#fff" stroke-width="8" stroke-linejoin="round"/>
    <polygon role="img" aria-label="Photo of hands reaching in from a dark sleeve" points="644,9 744,9 744,290 644,290 589,149" fill="url(#sleeveTone)" stroke="#fff" stroke-width="8" stroke-linejoin="round"/>
    <polygon role="img" aria-label="Photo of a dark sleeve from a group huddle" points="644,319 744,319 744,525 628,525 589,429" fill="#3a4150" stroke="#fff" stroke-width="8" stroke-linejoin="round"/>
  </svg>
  <div class="abs web-band">www.brightpath.example</div>
</section>

<section class="sheet inside">
  <svg class="abs" style="left:0;top:0" width="744" height="525" aria-hidden="true">
    <defs>
      <linearGradient id="chevronFade" x1="0" y1="1" x2="0" y2="0">
        <stop offset="0" stop-color="#739d8f" stop-opacity=".55"/>
        <stop offset="1" stop-color="#739d8f" stop-opacity="0"/>
      </linearGradient>
    </defs>
    <polygon points="48,525 170,525 360,150 300,30 240,30 290,150" fill="url(#chevronFade)"/>
  </svg>

  <div class="abs confidential-block"></div>
  <div class="abs photo-fade" role="img" aria-label="Faded photo of colleagues seated together in an office"></div>

  <div class="abs tab tab-sage" style="left:0;top:10px;width:245px">EMPLOYEE ASSISTANCE PROGRAM</div>
  <div class="abs copy" style="left:23px;top:47px;width:332px">
    <p>Employee Assistance Program (EAP) is a confidential employer-funded support service available to employees and immediate family members experiencing personal or work-related concerns. Immediate family include your spouse, partner, children or others living in your household.</p>
    <p>Brightpath provides a confidential and effective counselling process that is solution-focused and practical. The service is aimed at enhancing wellbeing and mental health, and can be accessed via face-to-face consultations, or by Telehealth or phone. Accessing assistance is an act of independence and strength which can empower you to make positive changes in your life.</p>
  </div>

  <div class="abs tab tab-salmon" style="left:0;top:160px;width:192px">COUNSELLING SERVICES</div>
  <div class="abs lead" style="left:23px;top:187px;width:320px">EAP is provided for a variety of personal, emotional and work-related matters including:</div>
  <div class="abs issues" style="left:37px;top:220px">
    <ul style="width:160px">
      <li>Anxiety</li><li>Depression and emotional wellbeing</li><li>Workplace conflict or disharmony</li><li>Coping with organisational change</li><li>Stress and burnout</li><li>Bullying</li><li>Sexual harassment</li><li>Self-esteem</li>
    </ul>
    <ul style="width:150px;padding-top:4px">
      <li style="height:28px">Reactions to traumatic or<br>&nbsp;&nbsp;distressing events</li><li>Critical incidents</li><li>Grief and bereavement</li><li>Substance misuse</li><li>Domestic violence</li><li>Interpersonal relationships</li><li>Schooling and study difficulties.</li>
    </ul>
  </div>
  <div class="abs copy" style="left:23px;top:353px;width:332px">
    <p>Brightpath also provides safe and culturally appropriate counselling services for culturally and linguistically diverse, Aboriginal and Torres Strait Islander and gender and sexually diverse (LGBTQIA+) employees.</p>
    <p>We want our clients to feel calm, confident and valued. We want them to know that they are in the best professional hands and that at every stage of the process they will be treated with respect and consideration. At the outset, you should know that you will be in a comfortable, completely confidential setting with a highly-trained, experienced professional who treats you with respect, helps you feel at ease and engages you deeply in the process.</p>
    <p>At Brightpath, we work hard to ensure that our clients have the best possible start and make continued progress in their therapy.</p>
  </div>

  <div class="abs tab tab-teal" style="left:371px;top:9px;width:206px">WHO PAYS FOR THE SERVICE?</div>
  <div class="abs copy" style="left:394px;top:44px;width:336px">
    <p>Your employer will pay for an agreed number of sessions. You are not required to pay for using the Brightpath EAP service. The number of available sessions depends on the agreement we have with your employer. On your first visit we will let you know how many sessions you can access. At the end of your last available session, your counsellor can discuss options for further counselling or support if needed.</p>
  </div>

  <div class="abs tab tab-teal" style="left:371px;top:121px;width:150px">IS IT CONFIDENTIAL?</div>
  <div class="abs copy" style="left:394px;top:156px;width:336px">
    <p>All employee personal information collated by Brightpath during the provision of counselling services will remain confidential and secure except when:</p>
    <ul class="conf-list">
      <li>&gt; It is subpoenaed by a court, or</li>
      <li>&gt; Failure to disclose the information would place the employee and/or another person at risk;<br><b>or</b></li>
      <li>&gt; The employee's prior consent has been obtained to:</li>
      <li class="sub">&gt; provide a written report to another professional or agency eg. The Employer, GP or lawyer; or</li>
      <li class="sub">&gt; discuss the material with another person eg. The Employer or GP.</li>
    </ul>
  </div>

  <div class="abs copy" style="left:394px;top:345px;width:336px;text-align:justify">Confidentiality and limitations of confidentiality are explained to employees at the beginning of the counselling process.</div>
  <div class="abs tab tab-sage" style="left:371px;top:385px;width:256px">HOW DO I MAKE AN EAP APPOINTMENT?</div>
  <div class="abs copy" style="left:394px;top:427px;width:336px">
    <p>The Brightpath intake team are trained in handling distressing incidents and will assist in making your initial appointment. We will respond to your call and book your initial appointment within the next working day, or at a time convenient to you.</p>
    <p>You can make a confidential appointment directly with Brightpath through our direct line on 03 9000 1234 or via hello@brightpath.example</p>
  </div>
</section>

</body>
</html>
```